Tavlune

I'd like new business card design options. I'll need to provide updated contact info although after the deign is complete. We are in IT, specifically in the data backup, archiving and disaster recovery verticals.

Business

```html
<!DOCTYPE html>
<html lang="en">
<head>
<meta charset="utf-8">
<title>Tavlune Business Card</title>
<link rel="stylesheet" href="https://fonts.googleapis.com/css2?family=Titillium+Web:wght@300;400;700&family=Saira+Condensed:wght@300;400&display=swap">
<style>
  :root {
    --page-bg: #eceef1;
    --card-bg: #ffffff;
    --brand-blue: #1f5fb8;
    --sky-blue: #4aa3dc;
    --name-blue: #2a78c8;
    --rule-blue: #8cc6ea;
    --band-light: #5db5e6;
    --band-light-end: #3d9dd9;
    --band-dark: #1556ab;
    --text-dark: #2e2e2e;
    --text-grey: #5a5a5a;
  }
  * { box-sizing: border-box; margin: 0; padding: 0; }
  html, body { width: 1200px; height: 1200px; overflow: hidden; }
  body { background: var(--page-bg); position: relative; font-family: "Titillium Web", sans-serif; }

  .business-card {
    position: absolute; left: 80px; top: 303px;
    width: 1040px; height: 594px;
    background: var(--card-bg);
    box-shadow: 0 14px 40px rgba(0,0,0,0.12);
    overflow: hidden;
  }

  .brand { position: absolute; left: 62px; top: 62px; display: flex; align-items: center; gap: 22px; }
  .brand-dot { width: 84px; height: 84px; border-radius: 50%; background: var(--sky-blue); }
  .brand-name {
    font-family: "Titillium Web", sans-serif; font-weight: 700;
    font-size: 64px; line-height: 1;
    color: var(--brand-blue);
  }

  .person { position: absolute; left: 232px; top: 196px; }
  .person-name {
    font-family: "Titillium Web", sans-serif; font-weight: 700;
    font-size: 50px; line-height: 1; letter-spacing: -1px;
    color: var(--name-blue);
  }
  .person-title { font-family: "Saira Condensed", sans-serif; font-weight: 300; font-size: 32px; color: var(--text-grey); line-height: 1.2; }

  .divider { position: absolute; left: 232px; right: 48px; top: 300px; height: 1px; background: var(--rule-blue); }

  .contact-list { position: absolute; left: 236px; top: 318px; list-style: none; }
  .contact-list li {
    display: flex; align-items: center; gap: 14px;
    font-weight: 300; font-size: 31px; line-height: 44px; color: var(--text-dark);
  }
  .contact-list svg { width: 26px; height: 26px; flex: none; }

  .address {
    position: absolute; right: 62px; top: 322px; text-align: right;
    font-family: "Saira Condensed", sans-serif; font-weight: 300;
    font-size: 27px; line-height: 36px; color: var(--text-dark);
  }
  .address-line { display: flex; justify-content: flex-end; align-items: center; gap: 6px; }
  .address svg { width: 18px; height: 22px; }

  .band-light {
    position: absolute; left: 0; bottom: 0; width: 64.5%; height: 56px;
    background: linear-gradient(90deg, var(--band-light-end), var(--band-light));
  }
  .band-dark {
    position: absolute; right: 0; bottom: 0; width: 36.5%; height: 92px;
    background: var(--band-dark);
    clip-path: polygon(22px 0, 100% 0, 100% 100%, 0 100%);
  }
</style>
</head>
<body>
  <div class="business-card">
    <div class="brand">
      <div class="brand-dot"></div>
      <div class="brand-name">Tavlune</div>
    </div>

    <div class="person">
      <div class="person-name">MARA QUINLAN</div>
      <div class="person-title">Director</div>
    </div>

    <div class="divider"></div>

    <ul class="contact-list">
      <li>
        <svg viewBox="0 0 24 24" aria-hidden="true"><path fill="#2a78c8" d="M6.6 10.8a15 15 0 0 0 6.6 6.6l2.2-2.2c.3-.3.7-.4 1-.2 1.1.4 2.3.6 3.6.6.6 0 1 .4 1 1V20c0 .6-.4 1-1 1A17 17 0 0 1 3 4c0-.6.4-1 1-1h3.5c.6 0 1 .4 1 1 0 1.3.2 2.5.6 3.6.1.3 0 .7-.2 1z"/></svg>
        1-555-014273
      </li>
      <li>
        <svg viewBox="0 0 24 24" aria-hidden="true"><circle cx="12" cy="12" r="10" fill="#2a78c8"/><path d="M2 12h20M12 2c3 3 3 17 0 20M12 2c-3 3-3 17 0 20" stroke="#fff" stroke-width="1.4" fill="none"/></svg>
        www.tavlune.com
      </li>
      <li>
        <svg viewBox="0 0 24 24" aria-hidden="true"><rect x="2" y="5" width="20" height="14" fill="#2a78c8"/><path d="M2 5l10 8 10-8" stroke="#fff" stroke-width="1.5" fill="none"/></svg>
        mara@tavlune.com
      </li>
    </ul>

    <div class="address">
      <div class="address-line">Dummy city
        <svg viewBox="0 0 18 22" aria-hidden="true"><path fill="#2a78c8" d="M9 0a8 8 0 0 0-8 8c0 6 8 14 8 14s8-8 8-14a8 8 0 0 0-8-8zm0 11a3 3 0 1 1 0-6 3 3 0 0 1 0 6z"/></svg>
      </div>
      <div>Dummy Country Land</div>
    </div>

    <div class="band-light"></div>
    <div class="band-dark"></div>
  </div>
</body>
</html>
```